NEED BILLBOARDS FOR VELMORANCIA

we need to redo our billboards for our business. we want to have catchy, great billboards that follow standard billboard design rules. we do breast and body cosmetic surgery in Bakersfield, fresno, and stockton ca. see attached for some tips. i would like something creative, but conservative, but funny. we also won finest around 18 years in a row and can give you the logo

Target Market(s)

females 21-45

Industry/Entity Type

plastic surgery of the breast and body

Font styles to use
Serif

Requirements
Nice to have
• funny, catchy
Should not have
• pictures of women that are overly exposed

```html
<!DOCTYPE html>
<html lang="en">
<head>
<meta charset="utf-8">
<title>Velmorancia Billboard</title>
<link href="https://fonts.googleapis.com/css2?family=Libre+Baskerville:wght@400;700&family=Poppins:wght@500;600&display=swap" rel="stylesheet">
<style>
  :root {
    --page: #e9ecf4;
    --blush-light: #fbe3df;
    --blush: #f6cfca;
    --circle: #f2aca7;
    --ink: #4a4141;
    --magenta: #dc4e8e;
    --magenta-light: #e45f97;
    --charcoal: #3a3131;
    --white: #ffffff;
    --hair-dark: #8a5f3f;
    --hair-light: #c69a72;
    --skin: #e8c1a8;
  }
  * { box-sizing: border-box; margin: 0; padding: 0; }
  html, body { width: 1200px; height: 935px; overflow: hidden; background: var(--page); }
  .canvas { position: relative; width: 1200px; height: 935px; }
  .billboard {
    position: absolute; left: 20px; top: 115px; width: 1160px; height: 705px;
    overflow: hidden;
    background: radial-gradient(ellipse at 60% 40%, var(--blush-light) 0%, var(--blush) 100%);
    box-shadow: 0 8px 24px rgba(60, 50, 70, 0.18);
  }
  .accent-circle { position: absolute; border-radius: 50%; background: var(--circle); }
  .accent-circle--left { left: 140px; top: -190px; width: 380px; height: 380px; opacity: 0.9; }
  .accent-circle--right { left: 880px; top: -80px; width: 380px; height: 380px; }
  .portrait {
    position: absolute; left: 0; top: 65px; width: 455px; height: 540px;
    border-radius: 48% 52% 10% 30% / 38% 40% 0 0;
    background: linear-gradient(160deg, var(--hair-light) 0%, var(--hair-dark) 45%, var(--skin) 80%, var(--hair-dark) 100%);
  }
  .serif { font-family: "Libre Baskerville", serif; font-weight: 700; color: var(--ink); }
  .brand-name {
    position: absolute; right: 50px; top: 128px;
    font-size: 40px; letter-spacing: 3px;
  }
  .award {
    position: absolute; right: 50px; top: 182px;
    font-size: 15px; letter-spacing: 1.5px;
  }
  .headline {
    position: absolute; left: 510px; top: 212px; width: 520px; text-align: center;
  }
  .headline__main { display: block; font-size: 96px; letter-spacing: 8px; line-height: 1; }
  .headline__sub { display: block; font-size: 40px; letter-spacing: 4px; line-height: 1.02; margin-top: 4px; }
  .services {
    position: absolute; left: 510px; top: 448px; width: 520px; text-align: center;
    font-size: 21px; letter-spacing: 2px;
  }
  .divider {
    position: absolute; left: 555px; top: 492px; width: 430px; height: 2px; background: var(--ink);
  }
  .website {
    position: absolute; left: 510px; top: 508px; width: 520px; text-align: center;
    font-size: 22px; letter-spacing: 3px;
  }
  .locations {
    position: absolute; left: 510px; top: 548px; width: 520px; text-align: center;
    font-size: 16px; letter-spacing: 2px;
  }
  .contact-band { position: absolute; left: 0; bottom: 0; width: 1160px; height: 118px; }
  .contact {
    position: absolute; bottom: 42px;
    font-family: "Poppins", sans-serif; font-weight: 600;
    font-size: 21px; letter-spacing: 2px; color: var(--white);
  }
  .contact--phone { left: 120px; }
  .contact--email { left: 450px; }
</style>
</head>
<body>
<div class="canvas">
  <section class="billboard">
    <div class="accent-circle accent-circle--left"></div>
    <div class="accent-circle accent-circle--right"></div>
    <div class="portrait" role="img" aria-label="Portrait photo of a woman with long wavy light-brown hair and red lipstick"></div>
    <div class="brand-name serif">VELMORANCIA</div>
    <p class="award serif">Finest Around · 18 Years in a Row</p>
    <h1 class="headline serif">
      <span class="headline__main">Beauty</span>
      <span class="headline__sub">from<br>the inside<br>out.</span>
    </h1>
    <p class="services serif">Breast &amp; Body Cosmetic Surgery</p>
    <div class="divider"></div>
    <p class="website serif">www.velmorancia.com</p>
    <p class="locations serif">Bakersfield · Fresno · Stockton</p>
    <svg class="contact-band" viewBox="0 0 1160 118" preserveAspectRatio="none" aria-hidden="true">
      <defs>
        <linearGradient id="bandFill" x1="0" x2="1" y1="0" y2="0">
          <stop offset="0" stop-color="var(--magenta)"/>
          <stop offset="1" stop-color="var(--magenta-light)"/>
        </linearGradient>
      </defs>
      <polygon points="0,0 1075,0 1010,118 0,118" fill="url(#bandFill)"/>
      <polygon points="1100,0 1160,0 1160,118 1035,118" fill="var(--charcoal)"/>
    </svg>
    <span class="contact contact--phone">(+012) 555 -0147</span>
    <span class="contact contact--email">hello@velmorancia.com</span>
  </section>
</div>
</body>
</html>
```